sydney wedding photography business needs a business card design

we need a business card design for a sydney based wedding photography and videography business. our business name is :golden hour photography and video. our target clients are 24-35 yrs female. our style is candid, organic, natural, dynamic. we are a team of young photographers and videographers, and help brides to create memories that they will cherish for the rest of their lives. the logo will be provided. we want an elegant design that reflects our style, and also want to give a great impression to our clients that we are one of the best studios in sydney and our brand means quality and premium service.

Target Market(s)

bride to be, 24-35 years old, living in sydney and surrunding areas

Industry/Entity Type

Wedding Photography

Contact Information for Business Card

address: 57 marrow lane, bexton nsw 2041
mobile: 0431872056
phone: (02) 9361 2748
info@goldenhourstudio.net.au
www.goldenhourstudio.net.au
facebook:goldenhourbridals
instagram:goldenhourbridals

Font styles to use
Serif
Sans Serif

Requirements
Nice to have
• maybe add my slogan"memories beyond eternity" if the layout looks good
Should not have
• no black color, not good idea for wedding biz card

```html
<!DOCTYPE html>
<html lang="en">
<head>
<meta charset="utf-8">
<title>Golden Hour Photography – Business Card</title>
<link rel="stylesheet" href="https://fonts.googleapis.com/css2?family=Fira+Sans:wght@400;500;600&display=swap">
<style>
  :root {
    --stage: #4d5157;
    --gold-deep: #8a5a1e;
    --gold-mid: #c9920e;
    --gold-bright: #ffcc00;
    --gold-text: #b07a0c;
    --bronze-ink: #3b2a12;
    --ivory: #f8f1e3;
    --ivory-warm: #efe2c6;
    --body-text: #4a3820;
  }
  * { box-sizing: border-box; margin: 0; padding: 0; }
  html, body {
    width: 1200px; height: 1200px; overflow: hidden;
    background: var(--stage);
    font-family: "Fira Sans", Arial, sans-serif;
  }
  .canvas {
    width: 1200px; height: 1200px;
    display: flex; flex-direction: column; align-items: center; justify-content: center;
    gap: 40px;
  }
  .card {
    position: relative;
    width: 900px; height: 514px;
    overflow: hidden;
    box-shadow: 0 10px 30px rgba(0,0,0,0.35);
  }

  /* Front */
  .card-front {
    background: linear-gradient(115deg, var(--gold-deep) 0%, var(--gold-mid) 28%, var(--gold-bright) 50%, var(--gold-mid) 74%, var(--gold-deep) 100%);
    display: flex; flex-direction: column; align-items: center; justify-content: center;
  }
  .front-name {
    font-weight: 600; font-size: 92px; color: var(--bronze-ink); line-height: 1;
  }
  .front-tagline {
    margin-top: 18px;
    font-weight: 400; font-size: 24px; letter-spacing: 16px; color: var(--bronze-ink);
    padding-left: 16px;
  }

  /* Back */
  .card-back {
    background: linear-gradient(135deg, var(--ivory) 0%, var(--ivory-warm) 100%);
  }
  .back-brand { position: absolute; left: 56px; top: 44px; }
  .back-name {
    font-weight: 600; font-size: 58px; color: var(--gold-text); line-height: 1;
  }
  .back-tagline {
    margin-top: 12px; margin-left: 70px;
    font-size: 18px; letter-spacing: 11px; color: var(--gold-text);
  }
  .ring-illustration {
    position: absolute; left: 30px; top: 230px; width: 440px; height: 284px;
    background: radial-gradient(ellipse at 50% 55%, rgba(201,146,14,0.35) 0%, rgba(201,146,14,0.18) 45%, rgba(201,146,14,0) 75%);
  }
  .details { position: absolute; left: 500px; top: 140px; }
  .detail-group {
    border-left: 2px solid var(--gold-text);
    padding-left: 26px;
    margin-bottom: 26px;
  }
  .person-name {
    font-weight: 500; font-size: 40px; color: var(--gold-text); line-height: 1.1;
  }
  .person-role { font-size: 18px; color: var(--body-text); margin-top: 6px; }
  .detail-line { font-size: 17px; color: var(--body-text); line-height: 1.55; }
  .accent-band {
    position: absolute; left: 505px; right: 0; bottom: 0; height: 22px;
    background: linear-gradient(90deg, var(--gold-mid), var(--gold-bright));
  }
</style>
</head>
<body>
<main class="canvas">
  <section class="card card-front" aria-label="Card front">
    <div class="front-name">Golden Hour</div>
    <div class="front-tagline">PHOTOGRAPHY</div>
  </section>

  <section class="card card-back" aria-label="Card back">
    <div class="back-brand">
      <div class="back-name">Golden Hour</div>
      <div class="back-tagline">PHOTOGRAPHY</div>
    </div>

    <div class="ring-illustration" role="img" aria-label="Faint gold illustration of a diamond engagement ring"></div>

    <div class="details">
      <div class="detail-group">
        <div class="person-name">JOHN DOE</div>
        <div class="person-role">Director</div>
      </div>
      <div class="detail-group">
        <div class="detail-line">57 Marrow Lane,</div>
        <div class="detail-line">Bexton NSW 2041</div>
      </div>
      <div class="detail-group">
        <div class="detail-line">M 0431 872 056 &nbsp;·&nbsp; P (02) 9361 2748</div>
        <div class="detail-line">www.goldenhourstudio.net.au</div>
        <div class="detail-line">info@goldenhourstudio.net.au</div>
        <div class="detail-line">facebook: goldenhourbridals</div>
        <div class="detail-line">instagram: goldenhourbridals</div>
      </div>
    </div>

    <div class="accent-band"></div>
  </section>
</main>
</body>
</html>
```